App UI design needed! For a Password Management Tool

Need a design of a Windows desktop application which is a Password Management Tool, similar to Vaultkin, Brimlock or Keywell, with Business/Enterprise functionalities. Here attached are a few sample pages of Brimlock, and some sample pages of our app called Tessaly. We certainly want to redesign our app.
We need: 1. The layout of the web: top banner, menu, main pane; 2. Form style, main form and sub forms; 3. List style; 4 Fonts and buttons; 5. Logo.
The design should look professional, can attract business customers as well as individual users, and present a strong sense of “Security”. The look and feel should differentiate from well-known products like Vaultkin, Brimlock, Keywell, etc.

```html
<!DOCTYPE html>
<html lang="en">
<head>
<meta charset="utf-8">
<title>Tessaly – Passwords</title>
<link href="https://fonts.googleapis.com/css2?family=Barlow:wght@400;500;600;700;800&display=swap" rel="stylesheet">
<style>
:root{
  --frame:#3b3b3d;
  --topstrip:#2c0a38;
  --header:#4b0d5e;
  --brand:#5f0a7c;
  --brand-soft:#8a1fa8;
  --lavender:#f2e0fd;
  --card-border:#e2b9f5;
  --icon-soft:#d58ff0;
  --ink:#1d1d1d;
  --muted:#7a7a7a;
  --panel:#f1f1f1;
  --sidebar:#f4f4f4;
  --line:#cfcfcf;
  --white:#ffffff;
  --welcome:#f3d6ff;
}
*{box-sizing:border-box;margin:0;padding:0}
html,body{width:1200px;height:830px;overflow:hidden;background:var(--frame);font-family:"Barlow",Arial,sans-serif}
.app{position:absolute;left:7px;top:7px;width:1186px;height:816px;background:var(--white);overflow:hidden}
.abs{position:absolute}
.top-strip{left:0;top:0;width:1186px;height:37px;background:var(--topstrip)}
.header{left:0;top:37px;width:1186px;height:72px;background:var(--header)}
.logo-box{left:0;top:0;width:268px;height:72px;background:var(--white);display:flex;align-items:center;justify-content:center}
.logo-name{font-weight:800;font-size:22px;letter-spacing:2px;color:var(--brand);text-transform:uppercase}
.welcome{left:298px;top:24px;font-size:16px;color:var(--welcome)}
.welcome b{font-weight:600;color:var(--white)}
.avatar{left:1084px;top:18px;width:37px;height:37px;border-radius:50%;background:var(--white);border:2px solid var(--icon-soft);display:flex;align-items:center;justify-content:center;font-weight:600;font-size:17px;color:var(--ink)}
.kebab{width:4px}
.kebab i{display:block;width:4px;height:4px;border-radius:50%;background:var(--white);margin-bottom:3px}
.category-band{left:0;top:109px;width:1186px;height:217px;background:var(--lavender)}
.category{background:var(--white);border:1.5px solid var(--card-border);border-radius:4px;display:flex;flex-direction:column;align-items:center}
.category.active{border:none;box-shadow:0 3px 10px rgba(120,40,160,.25);border-radius:6px}
.category-label{font-size:12px;color:var(--ink);position:absolute;bottom:24px;width:100%;text-align:center}
.category.active .category-label{font-size:20px;color:var(--brand);font-weight:500;bottom:28px}
.category.plain .category-label{font-weight:400}
.category.secure .category-label{font-weight:600}
.promo{left:718px;top:41px;width:404px;height:139px;background:linear-gradient(110deg,#2b1a6a 0%,#5a2aa0 45%,#3b2b8e 75%,#1e2a78 100%)}
.dots{left:913px;top:186px;display:flex;gap:3px}
.dots i{width:4px;height:4px;border-radius:50%;background:#b9b9c9}
.dots i:first-child{background:#555}
.tools-bar{left:0;top:326px;width:1186px;height:74px;background:var(--header)}
.tools-title{left:46px;top:27px;font-size:16px;color:var(--white);font-weight:500}
.search-zone{left:268px;top:0;width:313px;height:74px;background:var(--white)}
.search-zone::after{content:"";position:absolute;left:0;bottom:0;width:340px;height:3px;background:var(--brand-soft)}
.search-input{left:19px;top:17px;width:232px;height:42px;border:1.5px solid var(--card-border);border-radius:21px;background:#faf7fc;padding-left:18px;font-size:12px;color:#555;display:flex;align-items:center}
.add-btn{left:603px;top:21px;width:205px;height:36px;background:#6a1a86;border-radius:3px;display:flex;align-items:center;gap:12px;padding-left:14px;color:var(--white);font-size:16px;font-weight:600}
.sidebar{left:0;top:400px;width:268px;height:416px;background:var(--sidebar);border-right:2px solid #e2e2e2}
.tool{position:absolute;left:23px;width:222px;height:49px;border-bottom:1.5px solid var(--line);display:flex;align-items:center;gap:14px;padding-left:14px;font-size:12px;color:var(--ink)}
.tool.current{font-weight:700}
.form-panel{left:306px;top:426px;width:620px;height:277px;background:var(--panel)}
.form-head{left:0;top:0;width:620px;height:47px;background:var(--brand);color:var(--white);font-size:16px;font-weight:500;padding:15px 0 0 26px}
.line-field{left:25px;width:562px;height:42px;border-bottom:2px solid #9a9a9a;font-size:12px;color:var(--muted);padding:14px 0 0 25px}
.field-label{font-size:12px;color:var(--brand);font-weight:500;display:flex;align-items:center;gap:8px}
.box-field{height:38px;background:#f7f7f9;border:1.5px solid #dcdcdc;border-radius:5px}
.preview{left:926px;top:426px;width:220px;height:277px;background:var(--white);border:1px solid #dedede}
.save-btn{left:306px;top:711px;width:106px;height:34px;background:var(--brand);border-radius:2px;color:var(--white);font-size:12px;display:flex;align-items:center;justify-content:center}
</style>
</head>
<body>
<div class="app">
  <div class="abs top-strip"></div>

  <header class="abs header">
    <div class="abs logo-box"><span class="logo-name">Tessaly</span></div>
    <p class="abs welcome">Welcome Back <b>John!</b></p>
    <div class="abs avatar">J</div>
    <div class="abs kebab" style="left:1154px;top:24px"><i></i><i></i><i></i></div>
  </header>

  <section class="abs category-band">
    <div class="abs category active" style="left:63px;top:36px;width:151px;height:155px">
      <svg class="abs" style="left:44px;top:36px" width="68" height="48" viewBox="0 0 68 48">
        <rect x="0" y="12" width="68" height="24" fill="#e9c7f7"/>
        <path d="M24 20v-7a10 10 0 0 1 20 0v7" fill="none" stroke="#6a0a8a" stroke-width="5"/>
        <rect x="18" y="19" width="32" height="28" rx="3" fill="#6a0a8a"/>
        <circle cx="34" cy="33" r="3.5" fill="#fff"/>
      </svg>
      <span class="category-label">Passwords</span>
    </div>
    <div class="abs category secure" style="left:256px;top:45px;width:132px;height:134px">
      <svg class="abs" style="left:50px;top:35px" width="32" height="34" viewBox="0 0 32 34">
        <rect x="2" y="1" width="28" height="32" rx="3" fill="#d58ff0"/>
        <rect x="8" y="9" width="16" height="3" fill="#fff"/><rect x="8" y="16" width="16" height="3" fill="#fff"/><rect x="8" y="23" width="11" height="3" fill="#fff"/>
      </svg>
      <span class="category-label">Secure Notes</span>
    </div>
    <div class="abs category plain" style="left:400px;top:45px;width:132px;height:134px">
      <svg class="abs" style="left:48px;top:38px" width="36" height="28" viewBox="0 0 36 28">
        <rect x="2" y="2" width="32" height="24" rx="3" fill="none" stroke="#d58ff0" stroke-width="3"/>
        <rect x="2" y="8" width="32" height="5" fill="#d58ff0"/>
      </svg>
      <span class="category-label">Credit Cards</span>
    </div>
    <div class="abs category plain" style="left:544px;top:45px;width:132px;height:134px">
      <svg class="abs" style="left:48px;top:36px" width="36" height="34" viewBox="0 0 36 34">
        <circle cx="18" cy="10" r="7.5" fill="none" stroke="#d58ff0" stroke-width="3"/>
        <path d="M3 32v-3c0-6 7-9 15-9s15 3 15 9v3z" fill="none" stroke="#d58ff0" stroke-width="3"/>
      </svg>
      <span class="category-label">Personal Info</span>
    </div>
    <div class="abs promo" role="img" aria-label="Cyber security promotional banner with a padlock and key illustration"></div>
    <div class="abs dots"><i></i><i></i><i></i></div>
  </section>

  <section class="abs tools-bar">
    <p class="abs tools-title">Quick Tools</p>
    <div class="abs search-zone">
      <div class="abs search-input">Search for saved Passwords
        <svg class="abs" style="left:196px;top:12px" width="16" height="16" viewBox="0 0 16 16"><circle cx="6.5" cy="6.5" r="5" fill="none" stroke="#888" stroke-width="1.6"/><path d="M10.5 10.5 15 15" stroke="#888" stroke-width="1.6"/></svg>
      </div>
      <svg class="abs" style="left:275px;top:31px" width="14" height="10" viewBox="0 0 14 10"><path d="M0 1h14M3 5h8M5.5 9h3" stroke="#888" stroke-width="1.4"/></svg>
    </div>
    <div class="abs add-btn">
      <svg width="20" height="18" viewBox="0 0 20 18"><rect x="1" y="3" width="14" height="14" fill="#fff"/><rect x="4" y="7" width="8" height="1.6" fill="#6a1a86"/><rect x="4" y="10.5" width="8" height="1.6" fill="#6a1a86"/><path d="M17 0v6M14 3h6" stroke="#fff" stroke-width="1.8"/></svg>
      Add New Passwords
    </div>
    <div class="abs kebab" style="left:1154px;top:25px"><i></i><i></i><i></i></div>
  </section>

  <nav class="abs sidebar">
    <div class="tool current" style="top:4px">
      <svg width="12" height="14" viewBox="0 0 12 14"><path d="M3 6V4a3 3 0 0 1 6 0v2" fill="none" stroke="#222" stroke-width="1.8"/><rect x="1" y="6" width="10" height="8" rx="1" fill="#222"/></svg>
      Password Generator</div>
    <div class="tool" style="top:56px">
      <svg width="14" height="16" viewBox="0 0 14 16"><circle cx="7" cy="2" r="2" fill="#222"/><path d="M0 4.5h14v2H9V16H7.5v-5h-1v5H5V6.5H0z" fill="#222"/></svg>
      Password Health</div>
    <div class="tool" style="top:105px">
      <svg width="14" height="14" viewBox="0 0 14 14"><rect x="0" y="0" width="14" height="6" fill="#222"/><rect x="0" y="8" width="14" height="6" fill="#222"/><rect x="2" y="2" width="2" height="2" fill="#fff"/><rect x="2" y="10" width="2" height="2" fill="#fff"/></svg>
      Data Breach Scanner</div>
    <div class="tool" style="top:154px">
      <svg width="14" height="12" viewBox="0 0 14 12"><path d="M0 0h9l5 6-5 6H0l4-6z" fill="#222"/></svg>
      Emergency Access</div>
  </nav>

  <section class="abs form-panel">
    <div class="abs form-head">Save New Password</div>
    <div class="abs line-field" style="top:58px">Web Login Name</div>
    <div class="abs line-field" style="top:100px">Login URL (Optional)</div>
    <div class="abs field-label" style="left:43px;top:157px">
      <svg width="14" height="12" viewBox="0 0 14 12"><circle cx="5" cy="3" r="3" fill="#6a0a8a"/><path d="M0 12c0-4 3-5 5-5s5 1 5 5z" fill="#6a0a8a"/><path d="M9 5l1.5 1.5L14 3" stroke="#6a0a8a" stroke-width="1.4" fill="none"/></svg>Username</div>
    <div class="abs field-label" style="left:195px;top:157px">
      <svg width="14" height="12" viewBox="0 0 14 12"><rect x="0" y="0" width="14" height="12" rx="1" fill="#6a0a8a"/><path d="M1 1l6 5 6-5" stroke="#fff" stroke-width="1.3" fill="none"/></svg>Email Address</div>
    <div class="abs field-label" style="left:403px;top:157px">
      <svg width="12" height="14" viewBox="0 0 12 14"><path d="M3 6V4a3 3 0 0 1 6 0v2" fill="none" stroke="#6a0a8a" stroke-width="1.8"/><rect x="1" y="6" width="10" height="8" rx="1" fill="#6a0a8a"/></svg>Password</div>
    <div class="abs box-field" style="left:25px;top:178px;width:141px"></div>
    <div class="abs box-field" style="left:172px;top:178px;width:204px"></div>
    <div class="abs box-field" style="left:382px;top:178px;width:204px"></div>
  </section>

  <aside class="abs preview">
    <svg class="abs" style="left:84px;top:117px" width="68" height="48" viewBox="0 0 68 48">
      <rect x="0" y="10" width="68" height="24" fill="#e9c7f7"/>
      <path d="M24 20v-7a10 10 0 0 1 20 0v7" fill="none" stroke="#6a0a8a" stroke-width="5"/>
      <rect x="18" y="19" width="32" height="28" rx="3" fill="#6a0a8a"/>
      <circle cx="34" cy="33" r="3.5" fill="#fff"/>
    </svg>
  </aside>

  <div class="abs save-btn">Save</div>
</div>
</body>
</html>
```